Flyer für Immobilienmakler
Top Arbeit vom Designer. Er hat alle Idee schnell und professionell umgesetzt und das Ergebnis kann sich sehen lassen. Herzlichen Dank für die großartige Arbeit. Immer wieder gerne.
Zielgruppe
Immobilienmakler, Zielgruppe sind Menschen die uns weiterempfehlen um ihre Immobilie zu verkaufen
Aufgabenstellung
Ein Flyer DIN lang quer, Vorder und Rückseite, Es geht um eine Tippgeberprovision welche Menschen bekommen die uns einen Verkaufskunden bringen, diese erhalten 10 %- genaue Texte und Hinweise werde ich einbringen, Unser Slogan: 'Unsere Erfahrung für Ihren Vorteil'
Nachtrag. Bei dem Flyer 'Vom Berg Immobilien' finde ich die blauen Banner/ Streifen gut- ist aber kein Muss. Update: Es war als Inspiration von meiner Seite gedacht. Auf keinen Fall darf es genauso aussehen!!
Meine jetzige Webseite ist auch gut um die Farben zu erkennen, jedoch nicht unbedingt das Design, da ich gerade eine neue Webseite erstellen lasse

```html
<!DOCTYPE html>
<html lang="de">
<head>
<meta charset="utf-8">
<title>Novara Immobilien – Tippgeberprovision</title>
<link rel="stylesheet" href="https://fonts.googleapis.com/css2?family=Roboto+Condensed:wght@700&family=Montserrat:wght@600;700&display=swap">
<style>
  :root {
    --stage: #3a3a3a;
    --navy: #1e3566;
    --navy-deep: #1b2f60;
    --ink: #1f2d5c;
    --cream: #ece5da;
    --photo-sky: #7d8fa8;
    --photo-mid: #50678a;
    --photo-table: #dfe4ea;
    --band-light: #e9e7ee;
    --band-pink: #f2c6d0;
  }
  * { margin: 0; padding: 0; box-sizing: border-box; }
  html, body { width: 1200px; height: 1200px; overflow: hidden; }
  body { background: var(--stage); position: relative; }

  .flyer {
    position: absolute;
    left: 64px; top: 300px;
    width: 1082px; height: 540px;
    overflow: hidden;
    background: var(--navy);
    box-shadow: 8px 10px 18px rgba(0,0,0,0.45);
  }
  .hero {
    position: absolute; left: 0; top: 0;
    width: 100%; height: 444px;
    background: linear-gradient(90deg, var(--navy-deep) 0%, var(--navy) 100%);
  }
  .hero-photo {
    position: absolute; left: 0; top: 0;
    width: 820px; height: 444px;
    display: block;
  }
  .headline {
    position: absolute;
    left: 740px; top: 30px;
    transform: translateX(-50%);
    width: 700px;
    text-align: center;
    font-family: "Roboto Condensed", sans-serif;
    font-weight: 700;
    font-size: 70px;
    line-height: 72px;
    color: var(--cream);
  }
  .bonus {
    position: absolute;
    left: 795px; top: 206px;
    transform: translateX(-50%);
    font-family: "Montserrat", sans-serif;
    font-weight: 700;
    font-size: 125px;
    line-height: 1;
    color: var(--cream);
    white-space: nowrap;
  }
  .footer-band {
    position: absolute; left: 0; bottom: 0;
    width: 100%; height: 96px;
    background: linear-gradient(90deg, var(--band-light) 0%, var(--band-light) 22%, var(--band-pink) 45%, var(--band-pink) 100%);
  }
  .brand {
    position: absolute;
    left: 52px; top: 50%;
    transform: translateY(-50%);
    font-family: "Montserrat", sans-serif;
    font-weight: 600;
    font-size: 32px;
    color: var(--ink);
    white-space: nowrap;
  }
  .website {
    position: absolute;
    left: 686px; top: 50%;
    transform: translate(-50%, -50%);
    font-family: "Montserrat", sans-serif;
    font-weight: 600;
    font-size: 43px;
    letter-spacing: 2px;
    color: var(--ink);
    white-space: nowrap;
  }
</style>
</head>
<body>
  <div class="flyer">
    <div class="hero">
      <svg class="hero-photo" viewBox="0 0 820 444" role="img" aria-label="Foto: Hand stapelt Münzen zu wachsenden Türmen neben einem kleinen Hausmodell">
        <defs>
          <linearGradient id="photoTone" x1="0" y1="0" x2="0" y2="1">
            <stop offset="0" stop-color="var(--photo-mid)"/>
            <stop offset="0.45" stop-color="var(--photo-sky)"/>
            <stop offset="0.72" stop-color="#8e8a7a"/>
            <stop offset="0.84" stop-color="#c9ced6"/>
            <stop offset="1" stop-color="var(--photo-table)"/>
          </linearGradient>
          <linearGradient id="fadeRight" x1="0" y1="0" x2="1" y2="0">
            <stop offset="0" stop-color="#fff" stop-opacity="1"/>
            <stop offset="0.45" stop-color="#fff" stop-opacity="0.95"/>
            <stop offset="0.72" stop-color="#fff" stop-opacity="0.45"/>
            <stop offset="1" stop-color="#fff" stop-opacity="0"/>
          </linearGradient>
          <mask id="photoMask">
            <rect width="820" height="444" fill="url(#fadeRight)"/>
          </mask>
        </defs>
        <rect width="820" height="444" fill="url(#photoTone)" mask="url(#photoMask)"/>
      </svg>
      <h1 class="headline">Unsere Erfahrung für<br>Ihren Vorteil</h1>
      <p class="bonus">10 %</p>
    </div>
    <div class="footer-band">
      <span class="brand">Novara Immobilien</span>
      <span class="website">www.novara.immo</span>
    </div>
  </div>
</body>
</html>
```